Business Card for innovative, tech/consultant company

We are specializing in bringing together Efficiency methodology and Technology for our Business customers. We would like an astonishing business Card that matches this idea.

Target Market(s)

Businesses of medium size or more

Industry/Entity Type

Business Consultant

Contact Information for Business Card

Name, Title, personal email, www, address, phone

Font styles to use
Sans Serif

Colors
3277b5

Requirements
Must have
• - innovative, efficient design
• - good readable
• - Colors must match our logo (blue and grey)
• - the attached font (is licensed by our Company) must be used (Syntax LT)
Should not have
• overloaded

```html
<!DOCTYPE html>
<html lang="en">
<head>
<meta charset="utf-8">
<title>Veralink Business Card</title>
<link rel="stylesheet" href="https://fonts.googleapis.com/css2?family=Open+Sans:wght@400;600&display=swap">
<style>
  :root {
    --page-bg: #e9e6e1;
    --card-blue-light: #2fb0e0;
    --card-blue: #1f96cf;
    --card-blue-deep: #1478b4;
    --accent-grey: #9ea3a8;
    --text-white: #ffffff;
    --text-soft: rgba(255,255,255,0.85);
  }
  html, body {
    margin: 0;
    width: 1200px;
    height: 1022px;
    overflow: hidden;
    background: var(--page-bg);
    font-family: "Open Sans", Arial, sans-serif;
  }
  .canvas {
    position: relative;
    width: 1200px;
    height: 1022px;
    display: flex;
    align-items: center;
    justify-content: center;
  }
  .business-card {
    position: relative;
    width: 900px;
    height: 514px;
    border-radius: 22px;
    overflow: hidden;
    background: linear-gradient(160deg, var(--card-blue-light) 0%, var(--card-blue) 45%, var(--card-blue-deep) 100%);
    box-shadow: 0 18px 40px rgba(0,0,0,0.25);
  }
  .grey-tab {
    position: absolute;
    left: 0;
    bottom: 0;
    width: 22px;
    height: 150px;
    background: var(--accent-grey);
  }
  .brand-name {
    position: absolute;
    right: 70px;
    top: 150px;
    margin: 0;
    font-size: 150px;
    font-weight: 400;
    letter-spacing: -2px;
    color: var(--text-white);
    line-height: 1;
  }
  .contact-block {
    position: absolute;
    left: 60px;
    bottom: 56px;
    color: var(--text-white);
  }
  .person-name {
    margin: 0;
    font-size: 30px;
    font-weight: 600;
  }
  .person-title {
    margin: 2px 0 18px;
    font-size: 20px;
    color: var(--text-soft);
  }
  .contact-list {
    list-style: none;
    margin: 0;
    padding: 0;
    font-size: 19px;
    line-height: 30px;
  }
  .contact-list li {
    display: flex;
    align-items: center;
    gap: 12px;
  }
  .contact-list svg {
    width: 16px;
    height: 16px;
    flex: none;
    fill: none;
    stroke: var(--text-white);
    stroke-width: 1.6;
  }
</style>
</head>
<body>
<main class="canvas">
  <section class="business-card">
    <div class="grey-tab"></div>
    <h1 class="brand-name">Veralink</h1>
    <div class="contact-block">
      <p class="person-name">Mr Jonas Keller</p>
      <p class="person-title">Owner</p>
      <ul class="contact-list">
        <li>
          <svg viewBox="0 0 16 16"><path d="M4 1.5l2.5 3-1.5 1.5c.8 2 2.5 3.7 4.5 4.5l1.5-1.5 3 2.5-1.5 2.5C7 14 2 9 1.5 3z" fill="#fff" stroke="none"/></svg>
          <span>+330 2555-0142</span>
        </li>
        <li>
          <svg viewBox="0 0 16 16"><rect x="1.5" y="3.5" width="13" height="9"/><path d="M1.5 3.5l6.5 5 6.5-5"/></svg>
          <span>info@jonaskeller.com</span>
        </li>
        <li>
          <svg viewBox="0 0 16 16"><circle cx="8" cy="8" r="6.5"/><path d="M1.5 8h13M8 1.5c-3 3.5-3 9.5 0 13M8 1.5c3 3.5 3 9.5 0 13"/></svg>
          <span>www.keller-veralink.com</span>
        </li>
        <li>
          <svg viewBox="0 0 16 16"><path d="M8 15s-5-5.5-5-9a5 5 0 0 1 10 0c0 3.5-5 9-5 9z" fill="#fff" stroke="none"/><circle cx="8" cy="6" r="1.8" fill="#1f96cf" stroke="none"/></svg>
          <span>11, 8042 Lindenberg Switzerland</span>
        </li>
      </ul>
    </div>
  </section>
</main>
</body>
</html>
```